Label for a Rye Bourbon bottle

This new brand will be a High Rye Bourbon Finished in Port Casks, the name of the brand will be Stone Hollow.
Proof will be 90, alc. by vol. 45% Volume 750 ML

Would like the look and feel not too feel as traditional as many bourbon labels out there, something that could appeal to a more adventurous drinker, not your grandfather.

Target Market(s)

Bourbon and Whiskey drinking aficionados

```html
<!DOCTYPE html>
<html lang="en">
<head>
<meta charset="utf-8">
<title>Stone Hollow – High Rye Whiskey Label</title>
<link rel="stylesheet" href="https://fonts.googleapis.com/css2?family=Teko:wght@400;500&family=Playfair+Display:wght@800&family=Montserrat:wght@400;600&display=swap">
<style>
  :root {
    --paper: #ffffff;
    --label-black: #1b1b1a;
    --label-band: #24231f;
    --label-gold: #f1c894;
    --border-gold: #e6c08c;
    --wordmark-gold: #dba966;
    --barrel-tone: #cfcac2;
    --caption-ink: #222222;
  }
  html, body {
    margin: 0;
    padding: 0;
    width: 1200px;
    height: 930px;
    overflow: hidden;
    background: var(--paper);
  }
  .board { display: block; width: 1200px; height: 930px; }
  .label-body { fill: var(--label-black); }
  .label-border { fill: none; stroke: var(--border-gold); }
  .label-border--outer { stroke-width: 4; }
  .label-border--inner { stroke-width: 1.5; }
  .label-text { fill: var(--label-gold); }
  .type-display { font-family: "Teko", "Oswald", sans-serif; font-weight: 500; }
  .type-serif { font-family: "Playfair Display", Georgia, serif; font-weight: 800; }
  .type-small { font-family: "Montserrat", Arial, sans-serif; font-weight: 600; letter-spacing: 0.5px; }
  .rule { stroke: var(--label-gold); stroke-width: 1.6; }
  .pattern-band { fill: var(--label-band); }
  .barrel-art { fill: var(--barrel-tone); }
  .star-row { fill: var(--label-gold); }
  .proof-box { fill: none; stroke: var(--label-gold); stroke-width: 0.8; stroke-dasharray: 2 2; }
  .caption { font-family: "Montserrat", Arial, sans-serif; font-weight: 400; font-size: 10.5px; fill: var(--caption-ink); letter-spacing: 0.3px; }
  .wordmark { fill: var(--wordmark-gold); font-family: "Teko", "Oswald", sans-serif; font-weight: 500; }
</style>
</head>
<body>
<svg class="board" viewBox="0 0 1200 930" xmlns="http://www.w3.org/2000/svg">
  <g class="label" transform="translate(58 42)">
    <path class="label-body" d="M0 122 C20 120 40 112 48 100 L88 62 C110 45 130 40 150 35 C190 -8 270 -8 310 35 C330 40 350 45 372 62 L412 100 C420 112 440 120 460 122 C425 200 420 320 460 385 C440 390 420 396 405 410 C330 522 130 522 55 410 C40 396 20 390 0 385 C40 320 35 200 0 122 Z"/>
    <path class="label-border label-border--outer" transform="translate(230 270) scale(0.93 0.9) translate(-230 -255)" d="M0 122 C20 120 40 112 48 100 L88 62 L372 62 L412 100 C420 112 440 120 460 122 C425 200 420 320 460 385 C440 390 420 396 405 410 C330 522 130 522 55 410 C40 396 20 390 0 385 C40 320 35 200 0 122 Z"/>
    <path class="label-border label-border--inner" transform="translate(230 272) scale(0.895 0.865) translate(-230 -255)" d="M0 122 C20 120 40 112 48 100 L88 62 L372 62 L412 100 C420 112 440 120 460 122 C425 200 420 320 460 385 C440 390 420 396 405 410 C330 522 130 522 55 410 C40 396 20 390 0 385 C40 320 35 200 0 122 Z"/>

    <rect class="star-row" role="img" aria-label="Row of five small stars" x="192" y="18" width="76" height="5" rx="2.5"/>

    <g class="rules-top">
      <line class="rule" x1="140" y1="44" x2="178" y2="44"/>
      <line class="rule" x1="125" y1="52" x2="178" y2="52"/>
      <line class="rule" x1="110" y1="60" x2="178" y2="60"/>
      <line class="rule" x1="282" y1="44" x2="320" y2="44"/>
      <line class="rule" x1="282" y1="52" x2="335" y2="52"/>
      <line class="rule" x1="282" y1="60" x2="350" y2="60"/>
    </g>
    <text class="label-text type-display" x="230" y="66" font-size="34" text-anchor="middle" textLength="100" lengthAdjust="spacingAndGlyphs">RYE WHISKEY</text>

    <text class="label-text type-serif" x="230" y="126" font-size="21" text-anchor="middle" textLength="178" lengthAdjust="spacingAndGlyphs">FINISH IN PORT CASKS</text>

    <rect class="pattern-band" role="img" aria-label="Fine wave line pattern" x="40" y="145" width="380" height="62"/>
    <rect class="barrel-art" role="img" aria-label="Hand drawn whiskey barrel on its side" x="196" y="150" width="66" height="52" rx="22"/>

    <text class="label-text type-display" x="230" y="305" font-size="96" text-anchor="middle" textLength="334" lengthAdjust="spacingAndGlyphs">STONE HOLLOW</text>

    <line class="rule" x1="97" y1="340" x2="150" y2="340"/>
    <line class="rule" x1="310" y1="340" x2="363" y2="340"/>
    <text class="label-text type-display" x="230" y="350" font-size="28" text-anchor="middle" textLength="148" lengthAdjust="spacingAndGlyphs">HIGH RYE WHISKEY</text>

    <rect class="pattern-band" role="img" aria-label="Fine wave line pattern" x="45" y="362" width="370" height="18"/>

    <rect class="proof-box" x="151" y="394" width="160" height="26"/>
    <text class="label-text type-display" x="231" y="414" font-size="19" text-anchor="middle" textLength="137" lengthAdjust="spacingAndGlyphs">45% ALC BY VOL. 90 PROOF</text>
    <text class="label-text type-small" x="230" y="437" font-size="8.5" text-anchor="middle" textLength="170" lengthAdjust="spacingAndGlyphs">DISTILLED FROM LOCAL GROWN RYE</text>
    <text class="label-text type-display" x="230" y="462" font-size="19" text-anchor="middle" letter-spacing="1.5">750 ML</text>
  </g>

  <g class="caption-block">
    <text class="caption" x="387" y="598" text-anchor="middle">ORIGINAL VECTOR DESIGN | HAND MADE FONT | HAND DRAWN PICTURE | ORIGINAL CONCEPT</text>
    <text class="caption" x="387" y="616" text-anchor="middle">MADE IN ILLUSTRATOR | HIGH QUALITY DESIGN | LABELLING DESIGN | ANY CHANGES POSSIBLE | CONCEPT | MODERN</text>
  </g>

  <text class="wordmark" x="109" y="762" font-size="132" textLength="440" lengthAdjust="spacingAndGlyphs">STONE HOLLOW</text>
</svg>
</body>
</html>
```